7KiteX 2019 driving event needs an event poster!

We need a poster design advertising our driving event next June. I would like to see a whole range of classic, modern, colourful, perhaps even cartoon or stylish designs using our logos and event details such as web address, social media handles, dates and locations.

As an event poster, it needs to be informative and eye catching. You are the designer, make it interesting!

We have added our 2019 logo in various colours, and the banner of our facebook page, consider 7kitex.com which is our website which has many event details and ideas.

Event is 4 days. We drive through 3 countries starting in London, travelling through Wales, the lakes and into Scotland, finishing in Edinburgh.

Other similar and popular driving events that might give some ideas are pinwheel 4000, thunderbolt dash Europe, silverstorm cruise, etc

Colors

Designer to choose colors to be used in the design.

Requirements
Must have
• Eye-catching design. A cool look and feel. Perhaps a retro style. All ideas welcome.
Should not have
• A generic look and feel. Stolen images. Images I have to pay extra for. Something that looks like it took five minutes to slap together. No use of the word 'rally'. Its incredibly similar in all respects, but rally is a word that adds costs.

```html
<!DOCTYPE html>
<html lang="en">
<head>
<meta charset="utf-8">
<title>7KiteX 2019 Driving Event Poster</title>
<link rel="stylesheet" href="https://fonts.googleapis.com/css2?family=Alfa+Slab+One&display=swap">
<style>
  :root {
    --page-bg: #ece6db;
    --poster-dark: #3f3f3f;
    --poster-mid: #5a5a5a;
    --poster-light: #8a8a8a;
    --accent-yellow: #e9ed5b;
    --frame-yellow: #e3e24a;
    --text-white: #ffffff;
    --car-yellow: #f2c530;
    --car-silver: #d9d9d9;
    --badge-dark: #2b2b2b;
  }
  html, body {
    margin: 0;
    padding: 0;
    width: 1200px;
    height: 2560px;
    overflow: hidden;
    background: var(--page-bg);
  }
  .poster {
    position: absolute;
    left: 30px;
    top: 475px;
    width: 1140px;
    height: 1610px;
    box-shadow: 0 10px 30px rgba(0,0,0,0.25);
  }
  .poster svg {
    display: block;
    width: 1140px;
    height: 1610px;
  }
  .slab {
    font-family: "Alfa Slab One", "Rockwell", serif;
  }
  .headline { fill: var(--accent-yellow); }
  .intro { fill: var(--text-white); }
  .url-text { fill: var(--accent-yellow); }
  .info-label { fill: var(--accent-yellow); }
  .info-body { fill: var(--text-white); }
  .badge-name { fill: var(--text-white); }
</style>
</head>
<body>
<div class="poster">
  <svg viewBox="0 0 1140 1610" xmlns="http://www.w3.org/2000/svg">
    <defs>
      <radialGradient id="burstGlow" cx="0.74" cy="0.1" r="0.9">
        <stop offset="0" stop-color="var(--poster-light)"/>
        <stop offset="0.35" stop-color="var(--poster-mid)"/>
        <stop offset="1" stop-color="var(--poster-dark)"/>
      </radialGradient>
      <linearGradient id="carTones" x1="0" y1="0" x2="0" y2="1">
        <stop offset="0" stop-color="var(--car-yellow)"/>
        <stop offset="0.6" stop-color="#e0b325"/>
        <stop offset="1" stop-color="var(--car-silver)"/>
      </linearGradient>
    </defs>

    <!-- frame and background -->
    <rect class="poster-frame" x="0" y="0" width="1140" height="1610" fill="var(--frame-yellow)"/>
    <rect class="poster-field" x="22" y="22" width="1096" height="1566" fill="url(#burstGlow)"
          role="img" aria-label="Grey sunburst rays radiating from behind the car"/>

    <!-- website box -->
    <rect class="url-box" x="74" y="89" width="496" height="65" fill="none" stroke="var(--accent-yellow)" stroke-width="3"/>
    <text class="slab url-text" x="322" y="136" font-size="40" text-anchor="middle">www.7kitex.com</text>

    <!-- intro lines -->
    <text class="slab intro" x="74" y="250" font-size="100" textLength="496" lengthAdjust="spacingAndGlyphs">WE DRIVE</text>
    <text class="slab intro" x="74" y="340" font-size="100" textLength="490" lengthAdjust="spacingAndGlyphs">THROUGH</text>
    <text class="slab intro" x="74" y="418" font-size="66" textLength="490" lengthAdjust="spacingAndGlyphs">3 COUNTRIES</text>

    <!-- classic car illustration area -->
    <rect class="car-illustration" x="577" y="105" width="536" height="313" rx="60" fill="url(#carTones)"
          role="img" aria-label="Front view of a yellow classic convertible car with chrome grille and headlights"/>
    <g class="event-badge">
      <circle cx="845" cy="330" r="78" fill="var(--badge-dark)" stroke="var(--text-white)" stroke-width="5"/>
      <text class="slab badge-name" x="845" y="342" font-size="34" text-anchor="middle">7KiteX</text>
    </g>

    <!-- route headline -->
    <text class="slab headline" x="74" y="619" font-size="224" textLength="994" lengthAdjust="spacingAndGlyphs">STARTING</text>
    <text class="slab headline" x="74" y="776" font-size="188" textLength="994" lengthAdjust="spacingAndGlyphs">IN LONDON</text>
    <text class="slab headline" x="74" y="865" font-size="100" textLength="994" lengthAdjust="spacingAndGlyphs">TRAVELLING THROUGH</text>
    <text class="slab headline" x="74" y="954" font-size="103" textLength="994" lengthAdjust="spacingAndGlyphs">WALES, THE LAKES</text>
    <text class="slab headline" x="74" y="1055" font-size="108" textLength="994" lengthAdjust="spacingAndGlyphs">&amp; INTO SCOTLAND</text>
    <text class="slab headline" x="74" y="1223" font-size="203" textLength="994" lengthAdjust="spacingAndGlyphs">FINISHING</text>
    <text class="slab headline" x="74" y="1357" font-size="156" textLength="994" lengthAdjust="spacingAndGlyphs">IN EDINBURGH</text>

    <!-- event details -->
    <line class="info-divider" x1="548" y1="1390" x2="548" y2="1513" stroke="var(--text-white)" stroke-width="2"/>
    <g class="info-where">
      <text class="slab info-label" x="304" y="1424" font-size="30" text-anchor="middle">WHERE</text>
      <text class="slab info-body" x="304" y="1465" font-size="24" text-anchor="middle">DIAL CAFE, ORBITAL RING ROAD,</text>
      <text class="slab info-body" x="304" y="1499" font-size="24" text-anchor="middle">MILLBROOK, NW10 4QX LONDON, UK</text>
    </g>
    <g class="info-when">
      <text class="slab info-label" x="833" y="1424" font-size="30" text-anchor="middle">WHEN</text>
      <text class="slab info-body" x="833" y="1465" font-size="24" text-anchor="middle">27 JUNE 2019 AT 07:00 TO 30 JUNE 2019</text>
      <text class="slab info-body" x="833" y="1499" font-size="24" text-anchor="middle">AT 17:00 UTC+01</text>
    </g>

    <!-- social links -->
    <g class="social-links" fill="var(--accent-yellow)">
      <circle cx="522" cy="1553" r="16"/>
      <circle cx="570" cy="1553" r="16"/>
      <circle cx="618" cy="1553" r="16"/>
    </g>
  </svg>
</div>
</body>
</html>
```